Giving Porter

Need home page design for new website. The winner will have the opportunity to design the entire site.

I have attached 3 files.

1) Sort of a site map. PLEASE do not design the home page based on this wire frame. Be creative and use your expertise.

2) Tagline and Copy for the home page. Please just greek in or make up copy for areas that do not have copy at this time.

3) The logo.
Updates

Hi everyone, I am sorry for the delay. I have been out of town on unexpected business. I will make a decision this week. Thank you all for the great designs. Dale

Industry/Entity Type

Charity

```html
<!DOCTYPE html>
<html lang="en">
<head>
<meta charset="utf-8">
<title>Giving Porter — Successful, Not Stressful Fundraising</title>
<link rel="stylesheet" href="https://fonts.googleapis.com/css2?family=Fira+Sans:wght@300;400;600;700&display=swap">
<style>
  :root {
    --green: #3cad49;
    --green-soft: rgba(60, 173, 73, 0.82);
    --blue: #1f6f9c;
    --blue-soft: rgba(31, 111, 156, 0.88);
    --orange: #f0882a;
    --grey-band: #efefef;
    --text-grey: #7a7a7a;
    --text-dark: #333333;
    --white: #ffffff;
    --white-veil: rgba(255, 255, 255, 0.82);
  }
  * { box-sizing: border-box; margin: 0; padding: 0; }
  html, body { width: 1200px; height: 2362px; overflow: hidden; background: var(--white); }
  body { font-family: "Fira Sans", Arial, sans-serif; color: var(--text-grey); }
  .page { position: relative; width: 1200px; height: 2362px; overflow: hidden; }
  .abs { position: absolute; }

  /* Hero */
  .hero { position: absolute; left: 0; top: 0; width: 1200px; height: 951px; overflow: hidden; }
  .hero-photo {
    position: absolute; inset: 0;
    background: radial-gradient(ellipse at 62% 45%, #c98d6a 0%, #a8694a 30%, #6b4a3c 55%, #b7a9a6 80%, #d7c6cf 100%);
  }
  .hero-shapes { position: absolute; inset: 0; }
  .social-bar { position: absolute; left: 0; top: 0; width: 1200px; height: 35px; background: var(--green); }
  .social-icons { position: absolute; left: 566px; top: 10px; display: flex; gap: 12px; }
  .social-icons span { width: 15px; height: 15px; border-radius: 50%; background: var(--white); display: block; }
  .main-nav {
    position: absolute; left: 496px; top: 35px; width: 704px; height: 47px;
    background: rgba(255,255,255,0.92); display: flex; align-items: center; padding-left: 55px; gap: 36px;
    font-size: 17px; color: var(--text-dark);
  }
  .brand { position: absolute; left: 117px; top: 140px; display: flex; align-items: center; gap: 12px; }
  .brand-mark { width: 58px; height: 58px; border-radius: 50%; background: var(--green); }
  .brand-name { font-size: 30px; font-weight: 400; color: var(--green); }
  .headline-top { position: absolute; left: 509px; top: 118px; font-size: 72px; font-weight: 400; color: var(--green); line-height: 1; }
  .headline-bottom { position: absolute; left: 414px; top: 212px; color: var(--white); line-height: 1; white-space: nowrap; }
  .headline-bottom .light { font-size: 46px; font-weight: 300; }
  .headline-bottom .bold { font-size: 66px; font-weight: 700; margin-left: 10px; }
  .promo-title { position: absolute; left: 117px; top: 492px; font-size: 32px; color: var(--green); line-height: 1; }
  .promo-sub { position: absolute; left: 117px; top: 533px; font-size: 26px; font-weight: 300; color: var(--white); line-height: 1; }
  .promo-copy { position: absolute; left: 118px; top: 606px; width: 270px; font-size: 20px; font-weight: 300; line-height: 28px; color: var(--text-grey); }
  .btn {
    position: absolute; display: flex; align-items: center; justify-content: center;
    color: var(--white); clip-path: polygon(12% 0, 100% 0, 88% 100%, 0 100%);
  }
  .btn-read { left: 110px; top: 717px; width: 237px; height: 39px; background: var(--green); font-size: 19px; font-weight: 600; gap: 8px; }
  .btn-read .arrow-ring { width: 20px; height: 20px; border: 2px solid var(--white); border-radius: 50%; }
  .slider-dots { position: absolute; left: 945px; top: 823px; display: flex; gap: 8px; }
  .slider-dots span { width: 18px; height: 18px; border-radius: 50%; background: var(--white); }
  .slider-dots .active { background: var(--blue); border: 2px solid var(--white); }
  .btn-try { left: 304px; top: 860px; width: 342px; height: 66px; background: var(--orange); font-size: 32px; font-weight: 300; }
  .btn-demo-hero { left: 583px; top: 860px; width: 300px; height: 66px; background: var(--blue); font-size: 32px; font-weight: 300; }

  /* Section headings */
  .section-bar { position: absolute; left: 0; width: 1200px; height: 42px; background: var(--grey-band); }
  .section-bar .tag {
    position: absolute; left: 0; top: 0; height: 42px; display: flex; align-items: center; padding-left: 117px;
    color: var(--white); font-size: 25px; font-weight: 300;
    clip-path: polygon(0 0, 100% 0, 88% 100%, 0 100%);
  }

  /* About */
  .about-copy { position: absolute; font-size: 18px; font-weight: 300; line-height: 25px; color: var(--text-grey); }
  .art { position: absolute; }

  /* Testimonials */
  .testimonials { position: absolute; left: 0; top: 1641px; width: 1200px; height: 265px; overflow: hidden; }
  .testimonials-label {
    position: absolute; left: 0; top: 39px; width: 307px; height: 41px; background: rgba(255,255,255,0.85);
    clip-path: polygon(0 0, 100% 0, 88% 100%, 0 100%);
    padding-left: 117px; display: flex; align-items: center; font-size: 24px; color: var(--text-dark);
  }
  .nav-ring { position: absolute; width: 42px; height: 42px; border: 2px solid var(--white); border-radius: 50%; }
  .avatar { position: absolute; left: 321px; top: 73px; width: 126px; height: 126px; border-radius: 50%; border: 5px solid var(--white); background: linear-gradient(160deg, #8d6a55, #4a3a33); }
  .quote { position: absolute; left: 677px; top: 114px; width: 400px; font-size: 20px; line-height: 26px; color: var(--white); }
  .quote-mark { position: absolute; font-size: 80px; font-weight: 700; color: var(--white); line-height: 1; }

  /* Sign up */
  .signup-copy { position: absolute; left: 230px; top: 2070px; width: 740px; text-align: center; font-size: 19px; font-weight: 300; line-height: 27px; }
  .buttons-band { position: absolute; left: 0; top: 2192px; width: 1200px; height: 41px; background: var(--grey-band); }
  .btn-signup { left: 350px; top: 2186px; width: 245px; height: 47px; background: var(--blue); font-size: 24px; font-weight: 300; }
  .btn-demo { left: 543px; top: 2186px; width: 248px; height: 47px; background: var(--orange); font-size: 24px; font-weight: 300; }

  /* Footer */
  .site-footer { position: absolute; left: 0; top: 2315px; width: 1200px; height: 47px; background: var(--green); }
  .site-footer p { position: absolute; left: 118px; top: 14px; font-size: 17px; font-weight: 300; color: var(--white); }
  .footer-mark { position: absolute; left: 1047px; top: 8px; width: 32px; height: 32px; border-radius: 50%; background: var(--white); }
</style>
</head>
<body>
<div class="page">

  <header class="hero">
    <div class="hero-photo" role="img" aria-label="Photo of a smiling boy with a girl behind him"></div>
    <svg class="hero-shapes" width="1200" height="951" viewBox="0 0 1200 951">
      <polygon points="0,82 550,82 380,255 0,255" fill="rgba(255,255,255,0.82)"/>
      <polygon points="0,82 120,82 0,200" fill="rgba(60,173,73,0.75)"/>
      <polygon points="380,255 550,82 480,82 0,480 0,560" fill="rgba(60,173,73,0.45)"/>
      <polygon points="0,483 480,483 420,575 0,575" fill="rgba(31,111,156,0.9)"/>
      <polygon points="0,575 510,575 300,787 0,787" fill="rgba(255,255,255,0.82)"/>
      <polygon points="1200,510 1200,860 820,860" fill="rgba(60,173,73,0.88)"/>
      <polygon points="880,860 1200,860 1200,951 720,951" fill="rgba(60,173,73,0.9)"/>
      <polygon points="0,860 1200,860 1200,920 0,920" fill="rgba(255,255,255,0.85)"/>
    </svg>
    <div class="social-bar">
      <div class="social-icons"><span></span><span></span><span></span><span></span></div>
    </div>
    <nav class="main-nav">
      <span>Pricing</span><span>Features</span><span>Services</span><span>Products</span><span>About</span><span>Contact</span>
    </nav>
    <div class="brand"><span class="brand-mark"></span><span class="brand-name">GivingPorter.com</span></div>
    <h1>
      <span class="headline-top">Successful,</span>
      <span class="headline-bottom"><span class="light">Not Stressful</span><span class="bold">Fundraising</span></span>
    </h1>
    <p class="promo-title">CHARITY SUCCESS,</p>
    <p class="promo-sub">MINUS THE STRESS</p>
    <p class="promo-copy">Thinking about having a charity golf event but are turned off by the stress</p>
    <a class="btn btn-read"><span class="arrow-ring"></span>Read More</a>
    <div class="slider-dots"><span></span><span class="active"></span><span></span><span></span><span></span></div>
    <a class="btn btn-try">Try For Free</a>
    <a class="btn btn-demo-hero">Demo</a>
  </header>

  <section class="about">
    <div class="section-bar" style="top:1055px"><div class="tag" style="width:334px;background:var(--green)">Lorem Ipsum</div></div>
    <svg class="abs" style="left:0;top:1173px" width="1200" height="362" viewBox="0 0 1200 362">
      <polygon points="780,0 1200,0 1200,181 600,181" fill="#efefef"/>
      <polygon points="0,181 570,181 380,362 0,362" fill="#efefef"/>
    </svg>
    <p class="about-copy" style="left:117px;top:1195px;width:580px">If you are thinking about having a fundraiser, there is no better and more popular event than charity golf. But the time it takes to create invitations, registrations, banners, graphics, donors, as well as organizing and managing the entire event can be quite off-putting.</p>
    <div class="art" style="left:720px;top:1134px;width:375px;height:197px;border-radius:40% 40% 10% 10%;background:linear-gradient(180deg,#6aa84f 0%,#b8b08a 35%,#8c8f6a 100%)" role="img" aria-label="Illustration of a seedling growing from a pile of banknotes"></div>
    <div class="art" style="left:157px;top:1331px;width:197px;height:204px;background:linear-gradient(180deg,#3cad49 0%,#f2f2f2 40%,#dcdcdc 100%)" role="img" aria-label="Illustration of hands holding up coins"></div>
    <p class="about-copy" style="left:510px;top:1388px;width:553px;text-align:right">But don't put it off – PUTT it off! GivingPorter.com is the helping hand you need to create a great charity golf event that will be stress-free and, most importantly, help you raise money to achieve your goal.</p>
  </section>

  <section class="testimonials">
    <svg class="abs" style="left:0;top:0" width="1200" height="265" viewBox="0 0 1200 265" role="img" aria-label="Tinted backdrop of supporter portraits">
      <rect width="1200" height="265" fill="#3cad49"/>
      <polygon points="720,0 1200,0 1200,265 420,265" fill="#1f6f9c"/>
    </svg>
    <div class="testimonials-label">Testimonials</div>
    <span class="nav-ring" style="left:45px;top:110px"></span>
    <div class="avatar" role="img" aria-label="Portrait of a supporter"></div>
    <span class="quote-mark" style="left:625px;top:100px">“</span>
    <p class="quote">This is Photoshop's version of Lorem Ipsum. Proin gravida nibh vel velit auctor aliquet. Aenean sollicitudin, lorem quis bibend</p>
    <span class="quote-mark" style="left:1038px;top:170px">”</span>
    <span class="nav-ring" style="left:1113px;top:121px"></span>
  </section>

  <section class="signup">
    <div class="section-bar" style="top:1994px"><div class="tag" style="width:520px;background:var(--blue)">Sign Up Today for a Free Trial</div></div>
    <p class="signup-copy">This is Photoshop's version of Lorem Ipsum. Proin gravida nibh vel velit auctor aliquet. Aenean sollicitudin, lorem quis bibendum auctor, nisi elit consequat ipsum, nec sagittis sem nibh id</p>
    <div class="buttons-band"></div>
    <a class="btn btn-signup">Sign up</a>
    <a class="btn btn-demo">Demo</a>
  </section>

  <footer class="site-footer">
    <p>©2014. Giving Porter. All rights reserved</p>
    <span class="footer-mark"></span>
  </footer>

</div>
</body>
</html>
```